Real Estate 24"x24" Sign, Business Card, Letter Head and Envelope

This is a 4 project contest. If we choose a design or designs we like from what you sent we are willing to pay an amount at our discretion for that design even if we don't like all your designs for the 4 projects. Please be creative. Attached are our logo files. Please message us with any questions. Thanks and Good Luck!
Project 1: QLTV Realty 24" x 24" yard sign
We want to use the same blue background in our logo for the sign where the logo in white font will be on. CMYK 100,80,0,0. Attached is a sample a local designer made for you to get an idea what we are looking for. In the sample, the website is way too big and the entire sign is very plain and not attractive looking plus blue color is wrong one. We want the logo on top as large as possible but keeping it proportionate and attractive looking buy not too big that it looks odd. The following information can go in white color background or same blue color background color. Our company colors are blue (as per logo), green (as per logo), and white. "Residential & Commercial" goes under the logo. Under that put our phone number "312-948-6051" as large as possible but still looks good and under that our website in much smaller but readable font "www.qltvrealty.com".
Project 2: Envelope
We have two version of the logo. Use one or both. Whatever looks best in your design. The envelope will be white. We only want on top left corner logo and underneath our mailing address: 5197 Larchmere Ave. Skokie, IL 60093-1725. Maybe some creative decorative design at bottom of envelope will look nice
Project 3: Letter Head
We have two version of the logo. Use one or both. Whatever looks best in your design. We want the following information on the top of the letterhead. Logo, address: 5197 Larchmere Ave., Skokie, IL 60093-1725, phone: 312-948-6051, fax: 312-682-9307 website www.qltvrealty.com, email: info@qltvrealty.com
Project 4: Business card
Use either logo. We need cards for two individuals. Information for Person 1: Dev Kulkarni, Managing Broker, Phone: 312-948-6051, Email: dev.kulkarni@qltvrealty.com. Person 2: Ajay Kulkarni Broker Phone: 312-519-8263 Email: ajay.kulkarni@qltvrealty.com. Add Address, Fax and website same as above letter head.

```html
<!DOCTYPE html>
<html lang="en">
<head>
<meta charset="utf-8">
<title>QLTV Realty Stationery</title>
<link href="https://fonts.googleapis.com/css2?family=Jost:wght@400;500;600;700&display=swap" rel="stylesheet">
<style>
:root{
  --brand-blue:#034ea2;
  --brand-deep:#07407f;
  --ink-navy:#1d2a44;
  --body-gray:#8b8d91;
  --faint-mark:#e0e1e3;
  --paper:#ffffff;
  --stage-light:#eef0f2;
  --stage-edge:#d9dce1;
}
*{margin:0;padding:0;box-sizing:border-box}
html,body{width:1200px;height:1189px;overflow:hidden}
body{
  position:relative;
  font-family:"Jost",sans-serif;
  background:radial-gradient(ellipse at 50% 45%,var(--stage-light) 0%,var(--stage-edge) 100%);
}
.sheet{position:absolute;background:var(--paper);overflow:hidden}
.sheet svg.shape{position:absolute;left:0;top:0}

/* letterhead */
.letterhead{left:91px;top:80px;width:502px;height:718px}
.letterhead__header{position:absolute;left:0;top:0;width:100%;height:137px;background:var(--brand-blue);display:flex;align-items:center;justify-content:center}
.brand-name{font-family:"Jost",sans-serif;font-weight:600;letter-spacing:1px;white-space:nowrap}
.letterhead__brand{color:var(--paper);font-size:34px}
.letterhead__body{position:absolute;left:57px;top:180px;width:392px;font-size:11.6px;line-height:15px;color:var(--body-gray)}
.letterhead__body p{margin-bottom:14px}
.letterhead__sign{position:absolute;right:56px;top:532px;font-size:12.5px;color:#222}
.letterhead__sign-line{position:absolute;left:366px;top:571px;width:80px;border-top:1px solid #333}
.letterhead__footer{position:absolute;left:53px;top:656px;height:42px;border-left:1.5px solid var(--paper);padding-left:4px;color:var(--paper)}
.letterhead__footer .visit{font-size:8.5px;line-height:11px;margin-top:3px}
.letterhead__footer .addr{font-size:6.5px;line-height:8px;font-weight:500;margin-top:4px}

/* envelope */
.envelope-back{left:658px;top:211px;width:491px;height:197px}
.envelope-front{left:658px;top:440px;width:491px;height:196px}
.envelope-front__brand{position:absolute;left:25px;top:42px;font-size:20px;color:var(--brand-blue)}
.envelope-front__watermark{position:absolute;left:343px;top:20px;font-size:44px;line-height:44px;color:var(--faint-mark);text-align:right}
.envelope-front__watermark span{display:block;font-size:18px;line-height:22px;letter-spacing:3px}
.envelope-front__address{position:absolute;left:25px;top:162px;font-size:8px;line-height:10px;font-weight:500;color:var(--brand-blue)}

/* business cards */
.card{top:868px;width:355px;height:207px}
.card--dev{left:240px}
.card--ajay{left:646px}
.card__watermark{position:absolute;left:20px;top:56px;font-size:40px;line-height:44px;color:var(--faint-mark);text-align:right;width:138px}
.card__watermark span{display:block;font-size:16px;line-height:18px;letter-spacing:3px}
.card__name{position:absolute;left:31px;top:22px;font-size:19px;font-weight:700;color:var(--ink-navy);white-space:nowrap}
.card__title{position:absolute;left:31px;top:47px;font-size:10px;color:#5e6470;text-transform:uppercase}
.card__contact{position:absolute;left:217px;top:21px;height:110px;border-left:2px solid var(--brand-blue);padding-left:10px;color:var(--brand-blue);font-size:7.6px;line-height:10px}
.card__contact .email{margin-top:6px;white-space:nowrap;margin-left:-2px}
.card__contact .addr{margin-top:13px}
.card__contact .phone{margin-top:13px}
.card__contact .web{margin-top:20px}
</style>
</head>
<body>

<section class="sheet letterhead" aria-label="Letterhead">
  <div class="letterhead__header"><div class="brand-name letterhead__brand">QLTV REALTY</div></div>
  <div class="letterhead__body">
    <p>Solum nullam principes vis no, eleifend postulant mediocrem ut est, ad tota partem quo. Vix lorem putant scribentur no, mea meis solet melius no, pri feugait noluisse appetere no. Ei mea graece suscipit, fastidii probatus est et. Duo ut oportere iudicabit, exerci laoreet vim id. An vidit quidam cum, ceteros phaedrum sit ea. Mollis incorrupte in vix. Noster mnesarchum vix ei.</p>
    <p>Ius te maluisset voluptatum quaerendum, no discere saperet persequeris cum, no pro nonumy partem phaedrum. Mel mazim corpora te. Has ad aeque mucius impetus, vel tation regione appetere ne. Porro voluptatum ius ut, ei docendi eloquentiam sea. Ne mandamus dignissim efficiendi eum, est id tota insolens, eu per facete latine.</p>
    <p>Sea te explicari conceptam definitionem, soluta constituto duo ad, usu an laudem latine voluptaria. Eam magna repudiare forensibus an. In nam euismod explicari voluptatibus. Petentium dissentiet ex eum, in eam ludus tantas aperiam. Eu est latine feugait suavitate.</p>
    <p>Eum ei augue voluptua copiosae. Vis cu altera noluisse intellegat. At vis probatus perpetua. Tale alterum interesset ne quo, est ad exerci oblique recusabo, eu sit simul legendos antiopam. Qui tacimates tractatos ad, delectus sapientem omittantur ut vis. Pro te graece equidem ancillae, inductum molestiae eam ea.</p>
  </div>
  <div class="letterhead__sign">Signature</div>
  <div class="letterhead__sign-line"></div>
  <svg class="shape" width="502" height="718" viewBox="0 0 502 718" aria-hidden="true">
    <polygon points="0,588 502,700 502,718 0,718" fill="var(--brand-blue)"/>
    <polygon points="350,667 502,634 502,700" fill="var(--brand-deep)"/>
  </svg>
  <div class="letterhead__footer">
    <div class="visit">Visit us at</div>
    <div class="addr">5197 Larchmere Ave.,<br>Skokie, IL 60093-1725</div>
  </div>
</section>

<section class="sheet envelope-back" aria-label="Envelope back">
  <svg class="shape" width="491" height="197" viewBox="0 0 491 197" aria-hidden="true">
    <path d="M0,0 L224,91 Q245,100 266,91 L491,0 Z" fill="#8d8d8d" transform="translate(0,4)"/>
    <path d="M0,0 L224,91 Q245,100 266,91 L491,0 Z" fill="var(--brand-blue)"/>
  </svg>
</section>

<section class="sheet envelope-front" aria-label="Envelope front">
  <div class="brand-name envelope-front__brand">QLTV REALTY</div>
  <div class="brand-name envelope-front__watermark" aria-hidden="true">QLTV<span>REALTY</span></div>
  <div class="envelope-front__address">5197 Larchmere Ave. Skokie,<br>IL 60093-1725</div>
</section>

<section class="sheet card card--dev" aria-label="Business card, Dev Kulkarni">
  <div class="brand-name card__watermark" aria-hidden="true">QLTV<span>REALTY</span></div>
  <div class="card__name">Dev Kulkarni</div>
  <div class="card__title">Managing Broker</div>
  <div class="card__contact">
    <div class="email">dev.kulkarni@qltvrealty.com</div>
    <div class="addr">5197 Larchmere Ave., Skokie,<br>IL 60093-1725</div>
    <div class="phone">312-948-6051</div>
    <div class="web">qltvrealty.com</div>
  </div>
  <svg class="shape" width="355" height="207" viewBox="0 0 355 207" aria-hidden="true">
    <polygon points="0,116 246,171 355,148 355,207 0,207" fill="var(--brand-blue)"/>
    <polygon points="246,171 355,148 355,196" fill="var(--brand-deep)"/>
  </svg>
</section>

<section class="sheet card card--ajay" aria-label="Business card, Ajay Kulkarni">
  <div class="brand-name card__watermark" aria-hidden="true">QLTV<span>REALTY</span></div>
  <div class="card__name">Ajay Kulkarni</div>
  <div class="card__title">Broker</div>
  <div class="card__contact">
    <div class="email">ajay.kulkarni@qltvrealty.com</div>
    <div class="addr">5197 Larchmere Ave., Skokie,<br>IL 60093-1725</div>
    <div class="phone">312-519-8263</div>
    <div class="web">qltvrealty.com</div>
  </div>
  <svg class="shape" width="355" height="207" viewBox="0 0 355 207" aria-hidden="true">
    <polygon points="0,116 246,171 355,148 355,207 0,207" fill="var(--brand-blue)"/>
    <polygon points="246,171 355,148 355,196" fill="var(--brand-deep)"/>
  </svg>
</section>

</body>
</html>
```